Service business needs Business Card Design

Looking to create a new business card design that is both professional and unique the can highlight the many services we offer throughout the seasons. Our tagline is "The Cobalt Advantage"
Licensed & Insured: HC731462 has to be small and on the back side of the card.
On the Front:
FirstName LastName
Title
We offer the following services:
Deck Repair and Maintenance
Deck Cleaning and Staining/Painting
Power Washing/House Washing
Landscape Lighting Installation
Christmas Lighting Installation

```html
<!DOCTYPE html>
<html lang="en">
<head>
<meta charset="utf-8">
<title>Cobalt Crest Services – Business Cards</title>
<link href="https://fonts.googleapis.com/css2?family=Montserrat:wght@400;500;700;800&display=swap" rel="stylesheet">
<style>
  :root {
    --backdrop: #1d1d1f;
    --card: #ffffff;
    --navy: #0d4a8c;
    --sky: #3aa6dc;
    --ink: #1a1a1a;
  }
  * { margin: 0; padding: 0; box-sizing: border-box; }
  html, body {
    width: 1200px; height: 1200px; overflow: hidden;
    background: var(--backdrop);
    font-family: "Montserrat", Arial, sans-serif;
  }
  .stage {
    width: 1200px; height: 1200px;
    display: flex; flex-direction: column; align-items: center; justify-content: center;
    gap: 60px;
  }
  .card {
    width: 840px; height: 480px;
    background: var(--card);
    display: flex; flex-direction: column; align-items: center; justify-content: center;
    text-align: center;
  }
  .brand {
    display: flex; align-items: center; gap: 18px;
    color: var(--navy); font-weight: 800; letter-spacing: 2px;
    text-transform: uppercase;
  }
  .brand-dot { border-radius: 50%; background: var(--navy); flex: none; }
  .card--back .brand { font-size: 50px; }
  .card--back .brand-dot { width: 46px; height: 46px; }
  .license { margin-top: 34px; font-size: 20px; font-weight: 500; color: var(--ink); }

  .card--front .brand { font-size: 34px; }
  .card--front .brand-dot { width: 32px; height: 32px; }
  .person { margin-top: 22px; font-size: 34px; font-weight: 800; letter-spacing: 0.5px; }
  .person .first { color: var(--navy); }
  .person .last { color: var(--sky); }
  .role { font-size: 20px; font-weight: 500; color: var(--ink); margin-top: 2px; }
  .services-heading {
    display: flex; align-items: center; gap: 14px;
    margin-top: 16px; color: var(--navy); font-size: 28px; font-weight: 500;
  }
  .services-heading::before, .services-heading::after {
    content: ""; width: 150px; height: 2px; background: var(--navy);
  }
  .service-list {
    list-style: none; margin-top: 18px;
    display: grid; grid-template-columns: auto auto; column-gap: 34px; row-gap: 8px;
    font-size: 18px; font-weight: 500; color: var(--ink); text-align: left;
  }
  .service-list li { display: flex; align-items: center; gap: 10px; }
  .service-list li::before {
    content: ""; width: 11px; height: 11px; border-radius: 50%; background: var(--sky); flex: none;
  }
</style>
</head>
<body>
<main class="stage">
  <section class="card card--back">
    <div class="brand"><span class="brand-dot"></span>Cobalt Crest Services</div>
    <p class="license">Licensed &amp; Insured: HC731462</p>
  </section>

  <section class="card card--front">
    <div class="brand"><span class="brand-dot"></span>Cobalt Crest Services</div>
    <p class="person"><span class="first">DANIEL</span> <span class="last">FERROW</span></p>
    <p class="role">Co-Founder</p>
    <h2 class="services-heading">services</h2>
    <ul class="service-list">
      <li>Deck Repair and Maintenance</li>
      <li>Power Washing/House Washing</li>
      <li>Deck Cleaning and Staining/Painting</li>
      <li>Christmas Lighting Installation</li>
      <li>Landscape Lighting Installation</li>
    </ul>
  </section>
</main>
</body>
</html>
```